With over 10 years of experience as the president of Brightpath Access Group, LLC, we provide training and consulting services on various accessibility laws and standards, such as the ADA, Section 504, Fair Housing Act, and ANSI A117.1. My company specializes in helping agencies and commercial entities achieve compliance and create an inclusive environment for all customers.

In my role, I conduct ADA self-assessments, consult on transition plans, and deliver training on accessible design, program access, and reasonable accommodations. I use and develop skills such as public speaking, project management, and strategic problem-solving. I value collaboration, innovation, and diversity, and I strive to empower and support my clients and team members in reaching their accessibility goals.

https://brightpathaccessgroup.example/

Target Market(s)

See web site: https://brightpathaccessgroup.example/ or linked in for more language: https://www.linkedin.com/in/tom-hollis-572048163/

Industry/Entity Type

Education and consultative

Other font styles liked:
• Times New Roman

Requirements
Must have
• Specializes in ADA surveys, litigation assistance, construction consultation and transition plans.
Nice to have
• The photos I shared
Should not have
• Any other pictures or negative items

```html
<!DOCTYPE html>
<html lang="en">
<head>
<meta charset="utf-8">
<title>Brightpath Access Group — Training and Consulting Services</title>
<link rel="stylesheet" href="https://fonts.googleapis.com/css2?family=Tinos:wght@400;700&display=swap">
<style>
  :root{
    --page-bg:#d4d4d4;
    --paper:#ffffff;
    --brand-blue:#2a6db5;
    --ink:#1d1d1d;
    --panel:#f5f5f5;
    --rule:#d8d8d8;
    --orange:#f26a21;
    --red:#d9302c;
    --footer:#0f1a2b;
    --white:#ffffff;
  }
  *{margin:0;padding:0;box-sizing:border-box}
  html,body{width:1200px;height:1200px;overflow:hidden;background:var(--page-bg)}
  body{font-family:"Tinos","Times New Roman",serif;color:var(--ink)}
  .flyer{position:absolute;left:172px;top:0;width:856px;height:1200px;background:var(--paper);overflow:hidden}
  .top-band{position:absolute;left:0;top:0;width:856px;height:288px;background:var(--brand-blue)}
  .hero{position:absolute;left:71px;top:22px;width:713px;height:396px;border-radius:10px;
    background:linear-gradient(180deg,#6f8fb3 0%,#a9c0da 40%,#c9d8e8 70%,#e6edf5 100%)}
  .company{position:absolute;left:0;top:428px;width:856px;text-align:center;font-size:31px;font-weight:400;color:var(--ink)}
  .title{position:absolute;left:0;top:462px;width:856px;text-align:center;font-size:55px;font-weight:700;color:var(--brand-blue);letter-spacing:0.2px}
  .intro{position:absolute;left:43px;top:545px;width:783px;font-size:16.4px;line-height:20.9px;text-align:justify;text-align-last:center}
  .intro strong{font-weight:700}
  .services{position:absolute;left:0;top:690px;width:856px;height:339px;background:var(--panel)}
  .pill{position:absolute;height:42px;border-radius:5px;background:linear-gradient(90deg,var(--orange),var(--red));
    color:var(--white);font-weight:700;text-align:center;line-height:42px;white-space:nowrap}
  .specialisation{left:199px;top:669px;width:467px;font-size:37px}
  .col-divider{position:absolute;left:427px;top:730px;width:1px;height:285px;background:var(--rule)}
  .service h3{position:absolute;font-size:23px;font-weight:700;color:var(--brand-blue);white-space:nowrap}
  .service .photo{position:absolute;width:149px;height:100px;border-radius:4px}
  .service p{position:absolute;width:192px;font-size:16px;line-height:21px}
  .bottom-rule{position:absolute;left:0;top:1029px;width:856px;height:2px;background:var(--rule)}
  .footer{position:absolute;left:0;top:1040px;width:856px;height:160px;background:var(--footer);color:var(--white)}
  .contact{left:324px;top:14px;width:212px;font-size:38px}
  .footer-name{position:absolute;left:0;top:64px;width:856px;text-align:center;font-size:23px;font-weight:700}
  .footer-name span{font-size:15px;font-weight:400}
  .contact-row{position:absolute;left:30px;top:109px;width:690px;display:flex;gap:26px;align-items:center;font-size:14.5px}
  .contact-item{display:flex;align-items:center;gap:7px;white-space:nowrap}
  .contact-item svg{width:20px;height:20px;flex:none}
  .brand-box{position:absolute;left:733px;top:14px;width:93px;height:119px;background:var(--white);border-radius:6px;
    display:flex;align-items:center;justify-content:center;color:var(--brand-blue);font-size:18px;font-weight:700}
</style>
</head>
<body>
<div class="flyer">
  <div class="top-band"></div>
  <div class="hero" role="img" aria-label="Photo of a person in a wheelchair facing a street curb, with accessibility symbols and an accessibility shield overlaid"></div>

  <div class="company">Brightpath Access Group, LLC</div>
  <h1 class="title">Training and Consulting Services</h1>
  <p class="intro">We are experts on the application of the <strong>Americans with Disabilities Act (ADA)</strong> requirements for design and construction of public accommodation facilities. We have served hundreds of clients in and around the Ohio region, providing surveys and assessments to properties all over Ohio. We help lawyers, architects, property owners, and corporations and small businesses understand what needs to be in place to achieve ADA compliance so they are protected from litigation and have peace of mind and those unforseen drive-by lawsuits.</p>

  <div class="services"></div>
  <div class="pill specialisation">Our Area of Specialisation</div>
  <div class="col-divider"></div>

  <section class="service">
    <h3 style="left:30px;top:722px">On site Survey</h3>
    <div class="photo" style="left:30px;top:758px;background:linear-gradient(135deg,#e9e4dc,#a9a196 55%,#6f6a63)" role="img" aria-label="Photo of a team working at desks in a bright office, one member using a wheelchair"></div>
    <p style="left:195px;top:762px">After over 30 years, we only work with a select group of ADA and ICC certified Inspectors</p>
  </section>
  <section class="service">
    <h3 style="left:472px;top:722px">Litigation Assistance</h3>
    <div class="photo" style="left:472px;top:758px;background:linear-gradient(135deg,#b9875c,#5b7aa6 45%,#6b3d25)" role="img" aria-label="Photo of a civil code book beside a judge's gavel"></div>
    <p style="left:637px;top:762px">We can help you with a solution for your client’s ADA lawsuit</p>
  </section>
  <section class="service">
    <h3 style="left:30px;top:876px">Construction Consultation</h3>
    <div class="photo" style="left:30px;top:912px;background:linear-gradient(135deg,#c9a870,#8fa860 50%,#d9d6cf)" role="img" aria-label="Photo of contractors in hard hats and safety vests reviewing building plans"></div>
    <p style="left:195px;top:915px">Brightpath Access Group has a network of qualified contractors for your compliance construction</p>
  </section>
  <section class="service">
    <h3 style="left:472px;top:876px">Transition Plans</h3>
    <div class="photo" style="left:472px;top:912px;background:linear-gradient(135deg,#a8b2bf,#d8dbe0 50%,#8aa05a)" role="img" aria-label="Photo of a worker in a safety vest writing on a plan document"></div>
    <p style="left:637px;top:915px">We are on top on the project for start to finish ensuring that it is done correctly and On Time</p>
  </section>

  <div class="bottom-rule"></div>

  <footer class="footer">
    <div class="pill contact">Contact Us</div>
    <div class="footer-name">Brightpath Access Group, LLC <span>(Lakemont, Ohio)</span></div>
    <div class="contact-row">
      <div class="contact-item">
        <svg viewBox="0 0 20 20"><circle cx="10" cy="10" r="9" fill="none" stroke="#e8452c" stroke-width="1.5"/><path d="M7 5.5l2 2-1 1.3c.6 1.3 1.6 2.3 2.9 2.9l1.3-1 2 2-1.2 1.4c-3.3-.3-6.3-3.3-6.6-6.6z" fill="#fff"/></svg>
        <span>555-014-2738</span>
      </div>
      <div class="contact-item">
        <svg viewBox="0 0 20 20"><circle cx="10" cy="10" r="9" fill="none" stroke="#e8452c" stroke-width="1.5"/><rect x="5.5" y="6.5" width="9" height="7" fill="none" stroke="#fff" stroke-width="1.2"/><path d="M5.5 6.5l4.5 4 4.5-4" fill="none" stroke="#fff" stroke-width="1.2"/></svg>
        <span>info@brightpathaccessgroup.example</span>
      </div>
      <div class="contact-item">
        <svg viewBox="0 0 20 20"><circle cx="10" cy="10" r="9" fill="none" stroke="#e8452c" stroke-width="1.5"/><circle cx="10" cy="10" r="5" fill="none" stroke="#fff" stroke-width="1.1"/><ellipse cx="10" cy="10" rx="2" ry="5" fill="none" stroke="#fff" stroke-width="1.1"/><path d="M5 10h10" stroke="#fff" stroke-width="1.1"/></svg>
        <span>brightpathaccessgroup.example</span>
      </div>
    </div>
    <div class="brand-box">Brightpath</div>
  </footer>
</div>
</body>
</html>
```